Halvicek Law Group, PLLC
Business card and stationery
Professional
Marcus T. Halvicek, Esq.
President
248 Perrin Avenue
Suite 3407
New York, New York 10093
mhalvicek@halviceklawgroup.example
www.halviceklawgroup.example
Using Ivory-colored card stock
There are 2 additional staff members that need cards:
nothing

```html
<!DOCTYPE html>
<html lang="en">
<head>
<meta charset="utf-8">
<title>Halvicek Law Group, PLLC — Stationery</title>
<link rel="stylesheet" href="https://fonts.googleapis.com/css2?family=Montserrat:wght@400;700&family=Open+Sans:wght@400;600&display=swap">
<style>
:root{
  --stage:#d8d2c8;
  --ivory:#fffdf7;
  --maroon:#5b1b21;
  --maroon-text:#6e2a2f;
  --ink:#555;
  --soft:#999;
  --line:#d5d0c8;
}
*{box-sizing:border-box;margin:0;padding:0}
html,body{width:1200px;height:389px;overflow:hidden}
body{background:var(--stage);position:relative;font-family:"Open Sans",Arial,sans-serif;color:var(--ink)}
.piece{position:absolute;background:var(--ivory);box-shadow:0 2px 6px rgba(0,0,0,.25)}
.wordmark{font-family:"Montserrat",Arial,sans-serif;font-weight:700;color:var(--maroon-text);letter-spacing:.06em;line-height:1}
.tagline{font-family:"Montserrat",Arial,sans-serif;font-size:6px;letter-spacing:.25em;color:var(--soft);text-transform:uppercase}
.tiny{font-size:4px;line-height:1.5;color:var(--ink)}

/* brand lockup on stage */
.brand-lockup{position:absolute;left:84px;top:66px;text-align:center}
.brand-lockup .wordmark{font-size:40px}
.brand-lockup .tagline{font-size:8px;margin-top:6px}

/* business cards */
.card{width:154px;height:72px}
.card-front{left:19px;top:228px;display:flex;flex-direction:column;align-items:center;justify-content:center}
.card-front .wordmark{font-size:17px}
.card-front .tagline{font-size:4.5px;margin-top:3px}
.card-front .holder{font-size:4.5px;margin-top:6px;text-align:center;color:var(--ink)}
.card-back{left:182px;top:228px;padding:10px 10px}
.card-back .name{font-size:5px;font-weight:600;color:var(--maroon-text)}
.card-back .role{font-size:4px;color:var(--soft);margin-bottom:5px}
.card-back .cols{display:flex;justify-content:space-between}
.card-alt{left:19px;top:316px;height:60px;display:flex;flex-direction:column;align-items:center;justify-content:center}
.card-alt .wordmark{font-size:15px}
.card-dark{left:182px;top:316px;height:60px;background:var(--maroon);display:flex;flex-direction:column;align-items:center;justify-content:center}
.card-dark .wordmark{font-size:15px;color:var(--ivory)}
.card-dark .tagline{color:#d9c3c5;font-size:4.5px;margin-top:3px}
.card-alt .tagline{font-size:4.5px;margin-top:3px}

/* letterheads */
.sheet{width:178px;height:262px;top:96px;padding:14px 12px}
.letterhead{left:355px}
.fax{left:542px}
.sheet-head{display:flex;justify-content:space-between;align-items:flex-start}
.sheet-head .wordmark{font-size:13px}
.sheet-head .tagline{font-size:3.5px;margin-top:2px}
.sheet-head .tiny{text-align:right}
.sheet-foot{position:absolute;left:0;right:0;bottom:0;height:5px;background:var(--maroon)}
.body-lines{margin-top:26px}
.body-lines span{display:block;height:2px;background:#eee;margin-bottom:6px}
.fax-title{font-family:"Montserrat",Arial,sans-serif;font-size:7px;letter-spacing:.2em;color:var(--maroon-text);margin:14px 0 6px}
.fax-grid{display:grid;grid-template-columns:1fr 1fr;border-top:1px solid var(--line)}
.fax-grid div{font-size:4px;border-bottom:1px solid var(--line);padding:4px 2px;height:13px;color:var(--soft)}
.fax-grid div:nth-child(odd){border-right:1px solid var(--line)}
.fax-notes{margin-top:8px;font-size:4px;color:var(--soft)}

/* envelopes */
.envelope{left:883px;width:197px;height:78px}
.envelope-back{top:110px;overflow:hidden}
.envelope-back svg{position:absolute;left:0;top:0}
.envelope-front{top:196px;overflow:hidden}
.envelope-front svg{position:absolute;left:0;top:0}
.compliment{left:883px;top:288px;width:197px;height:72px;padding:10px 12px}
.compliment .wordmark{font-size:11px}
.compliment .tagline{font-size:3.5px;margin-top:2px}
.compliment .band{position:absolute;left:0;right:0;bottom:0;height:6px;background:var(--maroon)}
</style>
</head>
<body>

<div class="brand-lockup">
  <div class="wordmark">HALVICEK</div>
  <div class="tagline">Law Group, PLLC</div>
</div>

<div class="piece card card-front">
  <div class="wordmark">HALVICEK</div>
  <div class="tagline">Law Group, PLLC</div>
  <div class="holder">Marcus T. Halvicek, Esq. · President</div>
</div>

<div class="piece card card-back">
  <div class="name">Marcus T. Halvicek, Esq.</div>
  <div class="role">President</div>
  <div class="cols">
    <div class="tiny">248 Perrin Avenue<br>Suite 3407<br>New York, New York 10093</div>
    <div class="tiny">T (212) 555-0147<br>F (212) 555-0148<br>mhalvicek@halviceklawgroup.example<br>www.halviceklawgroup.example</div>
  </div>
</div>

<div class="piece card card-alt">
  <div class="wordmark">HALVICEK</div>
  <div class="tagline">Law Group, PLLC</div>
</div>

<div class="piece card card-dark">
  <div class="wordmark">HALVICEK</div>
  <div class="tagline">www.halviceklawgroup.example</div>
</div>

<div class="piece sheet letterhead">
  <div class="sheet-head">
    <div><div class="wordmark">HALVICEK</div><div class="tagline">Law Group, PLLC</div></div>
    <div class="tiny">248 Perrin Avenue, Suite 3407<br>New York, New York 10093<br>T (212) 555-0147<br>www.halviceklawgroup.example</div>
  </div>
  <div class="body-lines"><span></span><span></span><span></span><span style="width:70%"></span></div>
  <div class="sheet-foot"></div>
</div>

<div class="piece sheet fax">
  <div class="sheet-head">
    <div><div class="wordmark">HALVICEK</div><div class="tagline">Law Group, PLLC</div></div>
    <div class="tiny">248 Perrin Avenue, Suite 3407<br>New York, New York 10093<br>T (212) 555-0147<br>F (212) 555-0148</div>
  </div>
  <div class="fax-title">FAX</div>
  <div class="fax-grid">
    <div>To:</div><div>From:</div>
    <div>Fax:</div><div>Pages:</div>
    <div>Phone:</div><div>Date:</div>
    <div>Re:</div><div>CC:</div>
  </div>
  <div class="fax-notes">Comments:</div>
  <div class="sheet-foot"></div>
</div>

<div class="piece envelope envelope-back">
  <svg width="197" height="78" viewBox="0 0 197 78" aria-hidden="true">
    <path d="M0 0 H197 V22 L98.5 46 L0 22 Z" fill="var(--maroon)"/>
    <path d="M0 78 L98.5 40 L197 78" fill="none" stroke="var(--line)" stroke-width="1"/>
  </svg>
</div>

<div class="piece envelope envelope-front">
  <svg width="197" height="78" viewBox="0 0 197 78" aria-hidden="true">
    <path d="M0 0 L98.5 38 L197 0" fill="none" stroke="var(--line)" stroke-width="1"/>
    <path d="M0 78 L80 42 M197 78 L117 42" fill="none" stroke="var(--line)" stroke-width="1"/>
  </svg>
</div>

<div class="piece compliment">
  <div class="wordmark">HALVICEK</div>
  <div class="tagline">Law Group, PLLC</div>
  <div class="tiny" style="margin-top:10px">248 Perrin Avenue, Suite 3407 · New York, New York 10093</div>
  <div class="band"></div>
</div>

</body>
</html>
```